-------------- 概要 -------------- 会社で従業員に配布するための、名刺デザイン を募集します。 -------------------------- 依頼内容 -------------------------- ・サイズ:91×55mm ・素材の用意(画像・文章等):添付のロゴを使用してデザインください ・デザイン内容: ー横書き、横置きでお願いします ー表面:社名、役職、氏名、住所(〒347-0082 埼玉県草加市梢台3丁目6番12-905号) 、 携帯電話、メールアドレス(~~~@kz-w.co.jp)、ロゴ、HPのURL(https://www.kz-w.co.jp) ※( )の記載がない項目は仮置きでお願いできますでしょうか。 ー裏面:ロゴのみでよいと思っていますが、ぜひご意見、ご提案いただけると幸いです。 -------------------------- デザインイメージ -------------------------- ●ターゲット層: 企業で働く社会人向け(新人から部長層くらいまで)の研修を提供する会社です。直接の顧客は、その企業の人事部門となります。 ●雰囲気: 人事部門が相手となるため、信頼性と、社名にも込めた顧客のパートナーとして身近で温かみのあるイメージが伝わるとよいです。 コーポレートカラーは、【明るめの緑色】(添付の白抜きロゴの背景色)にしようと考えています。 研修での学習を通じて、人の成長が促されることを願っています。 また、会社が大事にしたいことを表すキーワードとしては、「共に」や「寄り添い」です。 ●ロゴの希望イメージの補足: 「伝統的⇔先進的」という選択項目は、先進的に近い方を選んでいますが 実際は「普遍的」というのも大事にしたいと思っています。 ただ、「伝統的」という言葉から想起されやすい”古さ”や”頑なさ”のようなイメージは 持ってほしくないと考えているため「先進的」にやや寄せました。 ●希望カラーの補足: 「緑系(安らぎ・平和・優しい)」選択しましたが、コーポレートカラーにする予定の 明るめの緑(黄緑、白抜きロゴの背景色)を使用していただきたいです。 ---------------- その他 ---------------- ※契約金額(税込)からシステム利用料を差し引いた金額が、ワーカーさまの受取金額となります その他ご質問等ありましたら、気軽にお問い合わせください。 ご応募をお待ちしております! |
以下のような要望に一番お応えいただいていたと感じたためです。
・表面については、肩書・名前・住所などの必要項目の記載が名刺右側にまとまっていたため、シンプルな印象や視認しやすい点がよかったです。
・また、表面において、ロゴも目立ちやすくよかったです。
・裏面についてはグラデーションや薄く白抜きしたロゴとのバランスがよく、シンプルさを保ちつつも、洗練された印象がよかったです。
全体的にシンプルでありつつも、古臭い感じではなく、先進的な印象も持てるデザインだったため、選択をさせていただきました。
素敵なデザインを提示いただきありがとうございました。
みなさま、ご提案をいただきありがとうございました。
どの案もこちらの要望にお応えいただいていたため、採用の決定については悩みました。
改めて、シンプルさと先進的(洗練された印象)のバランスのよさを最重視して選択をいたしました。

```html
<!DOCTYPE html>
<html lang="ja">
<head>
<meta charset="utf-8">
<title>KZ Weave 名刺デザイン</title>
<link rel="stylesheet" href="https://fonts.googleapis.com/css2?family=Noto+Serif+JP:wght@400;500&display=swap">
<style>
  :root {
    --brand-green: #6cb33f;
    --stage: #e4e4e4;
    --card-white: #ffffff;
    --ink: #2b2b2b;
    --ink-soft: #4a4a4a;
  }
  * { margin: 0; padding: 0; box-sizing: border-box; }
  html, body { width: 1200px; height: 1069px; overflow: hidden; }
  body {
    background: var(--stage);
    font-family: "Noto Serif JP", serif;
    color: var(--ink);
    position: relative;
  }
  .card {
    position: absolute;
    left: 245px;
    width: 710px;
    height: 432px;
  }
  .card-front {
    top: 83px;
    background: var(--card-white);
  }
  .card-front .accent-band {
    position: absolute;
    left: 0; top: 0; bottom: 0;
    width: 17px;
    background: var(--brand-green);
  }
  .brand {
    display: flex;
    align-items: center;
    gap: 12px;
    font-family: "Noto Serif JP", serif;
    font-weight: 500;
  }
  .brand-dot {
    border-radius: 50%;
    flex: none;
  }
  .card-front .brand {
    position: absolute;
    left: 82px;
    top: 44px;
    font-size: 32px;
    color: var(--ink-soft);
  }
  .card-front .brand-dot {
    width: 30px; height: 30px;
    background: var(--brand-green);
  }
  .person {
    position: absolute;
    left: 82px;
    top: 130px;
  }
  .person .role { font-size: 21px; letter-spacing: 0.04em; }
  .person .name {
    font-size: 46px;
    font-weight: 500;
    line-height: 1.2;
    margin-top: 4px;
    letter-spacing: 0.03em;
  }
  .person .name-roman { font-size: 17px; letter-spacing: 0.06em; margin-top: 2px; }
  .contact {
    position: absolute;
    left: 82px;
    top: 310px;
    list-style: none;
    font-size: 16.5px;
    color: var(--ink-soft);
  }
  .contact li {
    display: flex;
    align-items: center;
    gap: 10px;
    height: 27px;
  }
  .contact svg {
    width: 16px; height: 16px;
    fill: none;
    stroke: var(--brand-green);
    stroke-width: 2;
    flex: none;
  }
  .card-back {
    top: 582px;
    background: var(--brand-green);
    display: flex;
    align-items: center;
    justify-content: center;
  }
  .card-back .brand {
    color: var(--card-white);
    font-size: 44px;
    gap: 16px;
  }
  .card-back .brand-dot {
    width: 36px; height: 36px;
    background: var(--card-white);
  }
</style>
</head>
<body>
  <section class="card card-front" aria-label="名刺 表面">
    <div class="accent-band"></div>
    <div class="brand"><span class="brand-dot"></span>KZ Weave</div>
    <div class="person">
      <p class="role">代表取締役</p>
      <p class="name">佐藤 健一</p>
      <p class="name-roman">Kenichi Sato</p>
    </div>
    <ul class="contact">
      <li>
        <svg viewBox="0 0 16 16"><path d="M8 15s5-5 5-8.5A5 5 0 0 0 3 6.5C3 10 8 15 8 15z"/><circle cx="8" cy="6.5" r="1.8"/></svg>
        〒347-0082　埼玉県草加市梢台3丁目6番12-905号
      </li>
      <li>
        <svg viewBox="0 0 16 16"><path d="M3 2h3l1.5 3.5-2 1.3a8 8 0 0 0 3.7 3.7l1.3-2L14 10v3a1.5 1.5 0 0 1-1.5 1.5A11 11 0 0 1 1.5 3.5 1.5 1.5 0 0 1 3 2z"/></svg>
        ○○○-○○○○-○○○○
      </li>
      <li>
        <svg viewBox="0 0 16 16"><rect x="1.5" y="3.5" width="13" height="9" rx="1"/><path d="M1.5 4l6.5 5 6.5-5"/></svg>
        kenichi_sato@kz-w.co.jp
      </li>
      <li>
        <svg viewBox="0 0 16 16"><circle cx="8" cy="8" r="6.5"/><path d="M1.5 8h13M8 1.5c2 2 2 11 0 13M8 1.5c-2 2-2 11 0 13"/></svg>
        https://www.kz-w.co.jp
      </li>
    </ul>
  </section>

  <section class="card card-back" aria-label="名刺 裏面">
    <div class="brand"><span class="brand-dot"></span>KZ Weave</div>
  </section>
</body>
</html>
```